Animal Eye Clinic needs a Business card

We are a new veterinary ophthalmology practice (Tessaly Animal Eye Care) and we need a business card designed. We only see animal eyes - we are not a regular veterinary clinic. We already have a logo. We are looking for a professional, good looking business card to hand out to our clients. We are looking for something simple but professional and contemporary. Our logo is likely the only picture/graphic that needs to be on the card.
Updates

Contact Information for Business Card

Marisol Dunkley, BSc, DVM, MSc, DipACVO
Veterinary Ophthalmologist

Phone: 250.418.3097
Email: tessalyanimaleyecare@mailbrook.net
Website: tessalyanimaleyecare.net
Address: 1840 Pellworth Rd
Kelowna, BC, V4T 8M3

Colors

Designer to choose colors to be used in the design.

Requirements
Must have
• Our logo (attached)

```html
<!DOCTYPE html>
<html lang="en">
<head>
<meta charset="utf-8">
<title>Tessaly Animal Eye Care – Business Card</title>
<link href="https://fonts.googleapis.com/css2?family=Lato:wght@300;400;700;900&display=swap" rel="stylesheet">
<style>
  :root {
    --teal: #1b97a8;
    --slate: #737373;
    --ink: #666666;
    --paper: #ffffff;
    --backdrop: #2b2b2b;
  }
  html, body {
    margin: 0;
    padding: 0;
    width: 1200px;
    height: 900px;
    overflow: hidden;
    background: var(--backdrop);
    font-family: "Lato", sans-serif;
  }
  .canvas {
    position: relative;
    width: 1200px;
    height: 900px;
  }
  .card {
    position: absolute;
    width: 620px;
    height: 354px;
    border-radius: 22px;
    overflow: hidden;
    box-shadow: 0 10px 30px rgba(0,0,0,0.45);
  }

  /* Reverse side */
  .card-reverse {
    left: 70px;
    top: 50px;
    background: var(--teal);
  }
  .card-reverse .field {
    position: absolute;
    inset: 0;
  }
  .brand {
    position: absolute;
    display: flex;
    align-items: center;
    gap: 16px;
    color: var(--paper);
    font-weight: 700;
    line-height: 1;
  }
  .brand-dot {
    width: 58px;
    height: 58px;
    border-radius: 50%;
    background: currentColor;
    flex: none;
  }
  .brand-name {
    display: flex;
    flex-direction: column;
    gap: 6px;
  }
  .brand-top {
    letter-spacing: 0.55em;
  }
  .card-reverse .brand {
    left: 200px;
    top: 122px;
  }
  .card-reverse .brand-top { font-size: 22px; }
  .card-reverse .brand-bottom { font-size: 38px; }

  /* Front side */
  .card-front {
    left: 510px;
    top: 470px;
    background: var(--paper);
  }
  .card-front .brand {
    left: 40px;
    top: 36px;
    color: var(--teal);
    gap: 12px;
  }
  .card-front .brand-dot { width: 44px; height: 44px; }
  .card-front .brand-top { font-size: 14px; }
  .card-front .brand-bottom { font-size: 24px; }

  .person {
    position: absolute;
    left: 40px;
    top: 118px;
  }
  .person-name {
    margin: 0;
    color: var(--teal);
    font-weight: 900;
    font-size: 32px;
    line-height: 1;
  }
  .person-creds {
    margin: 4px 0 0;
    color: var(--ink);
    font-size: 9px;
    letter-spacing: 0.02em;
  }
  .person-role {
    margin: 3px 0 0;
    color: var(--ink);
    font-size: 15px;
    font-weight: 300;
  }
  .address {
    position: absolute;
    left: 40px;
    top: 196px;
    margin: 0;
    color: var(--ink);
    font-size: 15px;
    font-weight: 300;
    font-style: normal;
    line-height: 1.3;
  }
  .contact {
    position: absolute;
    left: 40px;
    top: 256px;
    margin: 0;
    padding: 0;
    list-style: none;
    color: var(--ink);
    font-size: 15px;
    font-weight: 300;
  }
  .contact li {
    display: flex;
    align-items: center;
    gap: 10px;
    height: 24px;
  }
  .contact svg {
    width: 14px;
    height: 14px;
    flex: none;
    fill: var(--teal);
  }
  .contact .accent { color: var(--teal); }
</style>
</head>
<body>
<main class="canvas">

  <section class="card card-reverse" aria-label="Business card, reverse side">
    <svg class="field" viewBox="0 0 620 354" preserveAspectRatio="none" aria-hidden="true">
      <path d="M205 0 H620 V300 C470 330 280 340 90 302 C120 180 150 80 205 0 Z" fill="#737373"/>
    </svg>
    <div class="brand">
      <span class="brand-dot" aria-hidden="true"></span>
      <span class="brand-name">
        <span class="brand-top">TESSALY</span>
        <span class="brand-bottom">ANIMAL EYE CARE</span>
      </span>
    </div>
  </section>

  <section class="card card-front" aria-label="Business card, front side">
    <div class="brand">
      <span class="brand-dot" aria-hidden="true"></span>
      <span class="brand-name">
        <span class="brand-top">TESSALY</span>
        <span class="brand-bottom">ANIMAL EYE CARE</span>
      </span>
    </div>

    <div class="person">
      <h1 class="person-name">Marisol Dunkley</h1>
      <p class="person-creds">BSc, DVM, MSc, DipACVO</p>
      <p class="person-role">Veterinary Ophthalmologist</p>
    </div>

    <address class="address">1840 Pellworth Rd<br>Kelowna, BC, V4T 8M3</address>

    <ul class="contact">
      <li>
        <svg viewBox="0 0 24 24" aria-hidden="true"><path d="M6.6 10.8a15 15 0 0 0 6.6 6.6l2.2-2.2c.3-.3.7-.4 1-.2 1.1.4 2.3.6 3.6.6.6 0 1 .4 1 1V20c0 .6-.4 1-1 1A17 17 0 0 1 3 4c0-.6.4-1 1-1h3.5c.6 0 1 .4 1 1 0 1.3.2 2.5.6 3.6.1.3 0 .7-.2 1z"/></svg>
        <span>250.418.3097</span>
      </li>
      <li>
        <svg viewBox="0 0 24 24" aria-hidden="true"><path d="M2 5h20v14H2z M4 7v.5l8 5 8-5V7l-8 5z" fill-rule="evenodd"/></svg>
        <span>tessalyanimaleyecare@mailbrook.net</span>
      </li>
      <li>
        <svg viewBox="0 0 24 24" aria-hidden="true"><path d="M12 2a10 10 0 1 0 0 20 10 10 0 0 0 0-20zm0 2c.9 0 2.2 1.9 2.7 5H9.3C9.8 5.9 11.1 4 12 4zm-3 7h6a16 16 0 0 1 0 2H9a16 16 0 0 1 0-2zm-4.9 0h2.9a18 18 0 0 0 0 2H4.1a8 8 0 0 1 0-2zm12.9 0h2.9a8 8 0 0 1 0 2H17a18 18 0 0 0 0-2zM9.3 15h5.4c-.5 3.1-1.8 5-2.7 5s-2.2-1.9-2.7-5z"/></svg>
        <span>www.<span class="accent">tessalyanimaleyecare</span>.net</span>
      </li>
    </ul>
  </section>

</main>
</body>
</html>
```